Masonry and Landscaping Construction company business card

Looking for a business card design for a construction company named Ferrano Construction. It is an italian-american family business that specializes in custom stone work, patios, walkways, driveways, steps, outdoor kitchens, concrete, waterproofing, power wash, landscaping and more. Our colors are mostly red and white with some black. We're looking for a bold design. we also like to incorporate a picture of my family's hometown somewhere in it.
Target Market(s)
Luxury home owners
Industry/Entity Type
Construction
Contact Information for Business Card
Details includes should be bullet points mentioning the services provided. Custom Stone Work, Outdoor Kitchens, Fire Pits, Patios, Walkways, Steps, Concrete, Waterproofing, powerwash and landscaping
Requirements
Must have
- Would like a spot on the card for co-owners names, numbers and email to be listed also looking to add the QR code for an instagram page
Nice to have
- would like something bold, based around the colors red and white with black outlines or details

```html
<!DOCTYPE html>
<html lang="en">
<head>
<meta charset="utf-8">
<title>Ferrano Construction – Business Card</title>
<link rel="stylesheet" href="https://fonts.googleapis.com/css2?family=Lato:wght@400;700;900&family=Orbitron:wght@800&display=swap">
<style>
  :root {
    --stage: #2b2b2d;
    --red: #d90a23;
    --black: #050505;
    --white: #ffffff;
    --green: #1fc24a;
    --silver-light: #f2f2f2;
    --silver-dark: #8a8a8a;
    --photo-sky: #c9d3dc;
    --photo-hill: #5f7d45;
    --photo-town: #b69a80;
  }
  * { box-sizing: border-box; margin: 0; padding: 0; }
  html, body { width: 1200px; height: 982px; overflow: hidden; }
  body {
    background: var(--stage);
    font-family: "Lato", sans-serif;
    position: relative;
  }
  .card {
    position: absolute;
    top: 171px;
    width: 380px;
    height: 640px;
    border-radius: 22px;
    overflow: hidden;
    box-shadow: 0 18px 40px rgba(0,0,0,.45);
  }
  .card--front { left: 170px; background: var(--red); }
  .card--back  { left: 650px; background: var(--black); }
  .card__shape { position: absolute; inset: 0; width: 100%; height: 100%; }

  /* Front */
  .services {
    position: absolute;
    left: 70px;
    top: 292px;
    list-style: none;
    color: var(--white);
    font-size: 18px;
    line-height: 24px;
    letter-spacing: .3px;
  }
  .services li { display: flex; align-items: center; gap: 12px; }
  .services .bullet {
    width: 14px; height: 14px; border-radius: 50%;
    background: var(--white); flex: none;
  }
  .brand-name {
    position: absolute;
    left: 0; right: 0;
    text-align: center;
    font-family: "Lato", sans-serif;
    font-weight: 900;
    text-transform: uppercase;
    line-height: 1;
  }
  .card--front .brand-name {
    bottom: 26px;
    color: var(--white);
    font-size: 28px;
    letter-spacing: 1px;
  }

  /* Back */
  .card--back .brand-name {
    top: 92px;
    color: var(--black);
    font-size: 32px;
    line-height: 1.05;
    letter-spacing: 1px;
  }
  .owner {
    position: absolute;
    top: 262px; left: 0; right: 0;
    text-align: center;
  }
  .owner__name {
    font-family: "Orbitron", sans-serif;
    font-weight: 800;
    color: var(--red);
    font-size: 28px;
    letter-spacing: 1px;
  }
  .owner__role {
    margin: 8px auto 0;
    width: 280px;
    display: flex; align-items: center; gap: 10px;
    color: var(--green);
    font-size: 17px;
  }
  .owner__role::before, .owner__role::after {
    content: ""; flex: 1; height: 1.5px; background: var(--green);
  }
  .contacts {
    position: absolute;
    top: 350px; left: 46px;
    list-style: none;
    color: var(--white);
    font-size: 17px;
  }
  .contacts li { display: flex; align-items: center; gap: 16px; height: 36px; }
  .contacts .icon {
    width: 28px; height: 28px; border-radius: 7px;
    background: var(--red);
    display: flex; align-items: center; justify-content: center; flex: none;
  }
  .divider {
    position: absolute; top: 545px; left: 170px;
    width: 40px; height: 1.5px; background: var(--green);
  }
  .address {
    position: absolute; top: 560px; left: 0; right: 0;
    text-align: center; color: var(--white);
    font-size: 16px; line-height: 22px; font-style: normal;
  }
</style>
</head>
<body>

<section class="card card--front">
  <svg class="card__shape" viewBox="0 0 380 640">
    <defs>
      <linearGradient id="photoTone" x1="0" y1="0" x2="0" y2="1">
        <stop offset="0" stop-color="var(--photo-sky)"/>
        <stop offset=".45" stop-color="var(--photo-hill)"/>
        <stop offset="1" stop-color="var(--photo-town)"/>
      </linearGradient>
      <linearGradient id="silverFront" x1="0" y1="0" x2="1" y2="0">
        <stop offset="0" stop-color="var(--silver-dark)"/>
        <stop offset=".5" stop-color="var(--silver-light)"/>
        <stop offset="1" stop-color="var(--silver-dark)"/>
      </linearGradient>
    </defs>
    <polygon points="0,0 380,0 380,214 190,284 0,214" fill="url(#silverFront)"/>
    <polygon points="0,0 380,0 380,200 190,270 0,200" fill="url(#photoTone)"
             role="img" aria-label="Photograph of the family's Italian hometown on a green hillside"/>
  </svg>
  <ul class="services">
    <li><span class="bullet"></span>Custom Stone Work</li>
    <li><span class="bullet"></span>Outdoor Kitchens</li>
    <li><span class="bullet"></span>Fire Pits</li>
    <li><span class="bullet"></span>Patios</li>
    <li><span class="bullet"></span>Walkways</li>
    <li><span class="bullet"></span>Steps</li>
    <li><span class="bullet"></span>Concrete</li>
    <li><span class="bullet"></span>Waterproofing</li>
    <li><span class="bullet"></span>Power Wash</li>
    <li><span class="bullet"></span>Landscaping &amp; More</li>
  </ul>
  <div class="brand-name">Ferrano<br>Construction</div>
</section>

<section class="card card--back">
  <svg class="card__shape" viewBox="0 0 380 640" aria-hidden="true">
    <defs>
      <linearGradient id="silverBack" x1="0" y1="0" x2="1" y2="0">
        <stop offset="0" stop-color="var(--silver-dark)"/>
        <stop offset=".5" stop-color="var(--silver-light)"/>
        <stop offset="1" stop-color="var(--silver-dark)"/>
      </linearGradient>
    </defs>
    <polygon points="0,0 380,0 380,190 190,250 0,190" fill="url(#silverBack)" transform="translate(0,12)"/>
    <polygon points="0,0 380,0 380,190 190,250 0,190" fill="var(--white)"/>
  </svg>
  <div class="brand-name">Ferrano<br>Construction</div>

  <div class="owner">
    <div class="owner__name">MARCO FERRANO</div>
    <div class="owner__role">Co-Owners</div>
  </div>

  <ul class="contacts">
    <li>
      <span class="icon"><svg width="16" height="16" viewBox="0 0 24 24"><path fill="#fff" d="M6.6 10.8a15 15 0 0 0 6.6 6.6l2.2-2.2a1 1 0 0 1 1-.25 11.4 11.4 0 0 0 3.6.57 1 1 0 0 1 1 1V20a1 1 0 0 1-1 1A17 17 0 0 1 3 4a1 1 0 0 1 1-1h3.5a1 1 0 0 1 1 1c0 1.25.2 2.45.57 3.57a1 1 0 0 1-.25 1z"/></svg></span>
      (123) 456-7890
    </li>
    <li>
      <span class="icon"><svg width="16" height="16" viewBox="0 0 24 24"><rect x="6" y="2" width="12" height="20" rx="2" fill="none" stroke="#fff" stroke-width="2"/><circle cx="12" cy="18" r="1.2" fill="#fff"/></svg></span>
      (123) 456-7890
    </li>
    <li>
      <span class="icon"><svg width="16" height="16" viewBox="0 0 24 24"><rect x="6" y="3" width="12" height="6" fill="#fff"/><rect x="3" y="9" width="18" height="8" rx="1.5" fill="#fff"/><rect x="7" y="14" width="10" height="7" fill="#fff" stroke="#d90a23" stroke-width="1.5"/></svg></span>
      (123) 456-7890
    </li>
    <li>
      <span class="icon"><svg width="16" height="16" viewBox="0 0 24 24"><rect x="2" y="5" width="20" height="14" rx="1.5" fill="#fff"/><path d="M2.5 6 12 13l9.5-7" fill="none" stroke="#d90a23" stroke-width="1.6"/></svg></span>
      info@yourwebsitehere.com
    </li>
    <li>
      <span class="icon"><svg width="16" height="16" viewBox="0 0 24 24"><circle cx="12" cy="12" r="9" fill="none" stroke="#fff" stroke-width="2"/><ellipse cx="12" cy="12" rx="4" ry="9" fill="none" stroke="#fff" stroke-width="1.6"/><path d="M3 12h18" stroke="#fff" stroke-width="1.6"/></svg></span>
      yourwebsitehere.com
    </li>
  </ul>

  <div class="divider"></div>
  <address class="address">
    423 Street Address Here, City<br>State &amp; Country, ZIP Code
  </address>
</section>

</body>
</html>
```